Landing page in the senior sector

We need a landing page for families looking for retirement homes for their parent. The target is rather old (50-60 years old). The mandatory fields are Name, Email, Phone. The optional fields are budget, research zipcode, Emergency (,,). It is important to note that this is a free service that we offer to families in research. It should be noted that they are often in distress and repulsive. Need a mobile landing We need a landing page to recruit families looking for retirement homes for their parent. The target is rather old (50-60 years old). Required fields are Name, Email, Phone. The optional fields (they may not appear at all) are Budget, Search CP, Emergency (,,). It is important to mention that this is a free service that we offer to families in search. It should be noted that they are often in distress and that asking them for input may let tel may seem repulsive. Also need a mobile version

Target Market(s)

rather old (50-60 years old) / rather old (50-60 years old)

Coding

Coded - Design and coding required

Number of Pages Required

2 page

Font styles to use
Sans Serif

Colors

Designer to choose colors to be used in the design.

Requirements
Must have
• - A form with the 3 mandatory fields / A form with the 3 mandatory fields - Optimized for conversion / Optimized for conversion

```html
<!DOCTYPE html>
<html lang="en">
<head>
<meta charset="utf-8">
<title>Evergreen Haven – Retirement Homes For Your Parents</title>
<link rel="stylesheet" href="https://fonts.googleapis.com/css2?family=Poppins:wght@400;500;600;700&display=swap">
<style>
  :root {
    --brand-blue: #0a4f85;
    --brand-green: #a8d523;
    --ink: #444444;
    --field-border: #c9c9c9;
    --panel: #f1f1f1;
    --footer: #000000;
    --white: #ffffff;
  }
  * { box-sizing: border-box; margin: 0; padding: 0; }
  html, body { width: 1097px; height: 1200px; overflow: hidden; }
  body { position: relative; font-family: "Poppins", sans-serif; background: var(--white); color: var(--ink); }

  .top-rule { position: absolute; left: 0; top: 0; width: 100%; height: 2px; background: var(--brand-green); z-index: 3; }

  .hero-photo {
    position: absolute; left: 0; top: 0; width: 1097px; height: 660px;
    background: linear-gradient(100deg, #5b4a45 0%, #7e6a60 25%, #8a8a92 45%, #6f7f96 60%, #9c8c7a 80%, #6e5a48 100%);
  }
  .hero-photo::after { content: ""; position: absolute; inset: 0; background: rgba(0,0,0,0.25); }
  .hero-edge { position: absolute; left: 0; top: 600px; width: 1097px; height: 60px; z-index: 2; }

  .brand { position: absolute; top: 52px; left: 0; width: 100%; display: flex; justify-content: center; align-items: center; gap: 12px; z-index: 3; }
  .brand-dot { width: 40px; height: 40px; border-radius: 50%; background: var(--brand-green); }
  .brand-name { font-size: 30px; font-weight: 700; color: var(--white); letter-spacing: 0.5px; }

  .hero-copy { position: absolute; left: 103px; top: 356px; width: 380px; color: var(--white); z-index: 3; }
  .hero-copy h1 { font-size: 40px; font-weight: 600; line-height: 1.2; white-space: nowrap; }
  .hero-copy p { margin-top: 12px; font-size: 12px; font-weight: 600; line-height: 22px; }

  .lead-form { position: absolute; left: 637px; top: 172px; width: 344px; height: 350px; background: var(--panel); border-radius: 3px; overflow: hidden; z-index: 3; }
  .lead-form header { background: var(--brand-blue); color: var(--white); text-align: center; height: 77px; padding-top: 12px; }
  .lead-form h2 { font-size: 24px; font-weight: 600; line-height: 1.2; }
  .lead-form header p { font-size: 13.5px; margin-top: 4px; }
  .field-grid { display: grid; grid-template-columns: 147px 148px; column-gap: 9px; row-gap: 12.5px; padding: 18px 20px 0; }
  .field { height: 34px; border: 1px solid var(--field-border); background: var(--white); font-family: inherit; font-size: 11.5px; color: #666; padding: 0 14px; display: flex; align-items: center; justify-content: space-between; }
  .field .caret { width: 0; height: 0; border-left: 4px solid transparent; border-right: 4px solid transparent; border-top: 4px solid #777; }
  .submit { display: block; margin: 21px auto 0; width: 134px; height: 35px; border: none; border-radius: 18px; background: var(--brand-blue); color: var(--white); font-family: inherit; font-size: 13.5px; font-weight: 600; }

  .about { position: absolute; top: 716px; left: 0; width: 100%; text-align: center; }
  .about h2 { font-size: 40px; font-weight: 600; color: var(--brand-blue); line-height: 1.3; }
  .about p { width: 790px; margin: 18px auto 0; font-size: 14.4px; line-height: 26.5px; color: var(--ink); }
  .read-more { display: block; margin: 28px auto 0; width: 179px; height: 45px; border-radius: 23px; background: var(--brand-blue); color: var(--white); font-size: 14px; font-weight: 600; line-height: 45px; text-decoration: none; }

  .footer { position: absolute; left: 0; top: 1026px; width: 100%; height: 174px; }
  .footer-edge { position: absolute; left: 0; top: 0; width: 1097px; height: 174px; }
  .social { position: absolute; top: 64px; left: 0; width: 100%; display: flex; justify-content: center; gap: 8px; }
  .social span { width: 29px; height: 29px; border: 2px solid var(--white); border-radius: 50%; }
  .legal { position: absolute; top: 114px; width: 100%; text-align: center; color: var(--white); font-size: 13px; }
</style>
</head>
<body>
  <div class="top-rule"></div>

  <div class="hero-photo" role="img" aria-label="Photo of smiling seniors gathered around a table with a laptop in a bright dining room"></div>
  <svg class="hero-edge" viewBox="0 0 1097 60" preserveAspectRatio="none" aria-hidden="true">
    <polygon points="0,12 549,52 1097,12 1097,60 0,60" fill="#ffffff"/>
    <polygon points="0,14 549,50 1097,14 1097,19 549,56 0,19" fill="#a8d523"/>
  </svg>

  <div class="brand">
    <span class="brand-dot"></span>
    <span class="brand-name">EVERGREEN HAVEN</span>
  </div>

  <div class="hero-copy">
    <h1>We Offer Free Service</h1>
    <p>Lorem ipsum dolor sit amet, consectetur adipiscing elit, sed do eiusmod tempor incididunt ut labore et dolore magna aliqua.</p>
  </div>

  <form class="lead-form">
    <header>
      <h2>Get In Touch</h2>
      <p>Retirement Homes For Your Parents</p>
    </header>
    <div class="field-grid">
      <div class="field">*First Name</div>
      <div class="field">*First Name</div>
      <div class="field">*Email</div>
      <div class="field">*Phone Number</div>
      <div class="field">Budget</div>
      <div class="field">Search CP</div>
      <div class="field">Zipcode <span class="caret"></span></div>
      <div class="field">Emergency</div>
    </div>
    <button type="button" class="submit">Submit</button>
  </form>

  <section class="about">
    <h2>About Us</h2>
    <p>Sed ut perspiciatis unde omnis iste natus error sit voluptatem accusantium doloremque laudantium, totam rem aperiam, eaque ipsa quae ab illo inventore veritatis et quasi architecto beatae vitae dicta sunt explicabo. Nemo enim ipsam voluptatem quia voluptas sit aspernatur aut odit aut fugit, sed quia consequuntur magni dolores eos qui ratione voluptatem sequi nesciunt.</p>
    <a class="read-more" href="#">Read More</a>
  </section>

  <footer class="footer">
    <svg class="footer-edge" viewBox="0 0 1097 174" preserveAspectRatio="none" aria-hidden="true">
      <polygon points="0,42 549,6 1097,42 1097,174 0,174" fill="#000000"/>
      <polygon points="0,37 549,0 1097,37 1097,44 549,8 0,44" fill="#0a4f85"/>
    </svg>
    <div class="social">
      <span aria-label="Social link"></span>
      <span aria-label="Social link"></span>
      <span aria-label="Social link"></span>
    </div>
    <p class="legal">Copyright 2018 | All Rights Reserved | Privacy Policy | Term &amp; Conditions</p>
  </footer>
</body>
</html>
```